A wine Label for a new brand of New Zealand Wine

We are looking for a Wine Label for our "Harbor Crest" brand of wines from North Otago New Zealand. We would like the label to perhaps use the HC as a logo and the rest up to the designer. We have our vineyards located in the Waitaki Valley New Zealand which is a southern region with mountains and a river flowing past our vineyard. Photos attached of Dramatic Landscape. Also attached is a basic outline of requirements for the front bottle of the label. The rear bottle label will contain writing about the wines background plus statutory regulations on Alc. Vol, bar code etc. Front Label size to be no Larger than 80mm deep by 100 mm wide. The label can be simple or graphic, whatever the designer chooses.
Target Market(s)
New Wine Brand
Look and feel
Each slider illustrates characteristics of the customer's brand and the style your logo design should communicate.

```html
<!DOCTYPE html>
<html lang="en">
<head>
<meta charset="utf-8">
<title>Harbor Crest – Pinot Gris Front Label</title>
<link rel="stylesheet" href="https://fonts.googleapis.com/css2?family=Cinzel:wght@500;600;700&family=Libre+Baskerville:wght@400;700&family=Pinyon+Script&display=swap">
<style>
  :root {
    --backdrop: #353535;
    --sky-top: #d6e9f6;
    --sky-bottom: #f4f8fb;
    --gold: #c9a24a;
    --gold-line: #d2ae5a;
    --ink: #1e1e1e;
    --ink-soft: #3a3a3a;
    --flourish: #9a9a9a;
    --mountain: #c9cbcc;
    --mountain-shade: #a9acad;
    --vine-light: #9cc25a;
    --vine-dark: #4f7a2c;
  }
  * { margin: 0; padding: 0; box-sizing: border-box; }
  html, body {
    width: 1200px;
    height: 1111px;
    overflow: hidden;
    background: var(--backdrop);
  }
  .canvas {
    position: relative;
    width: 1200px;
    height: 1111px;
  }
  .label {
    position: absolute;
    left: 215px;
    top: 75px;
    width: 770px;
    height: 960px;
    background: linear-gradient(180deg, var(--sky-top) 0%, var(--sky-bottom) 55%, #eef3f6 62%);
    box-shadow: 0 12px 30px rgba(0,0,0,0.45);
    overflow: hidden;
    text-align: center;
  }
  .brand-mark {
    position: absolute;
    left: 304px;
    top: 27px;
    width: 162px;
    height: 180px;
    border: 3px solid var(--gold-line);
    display: flex;
    align-items: center;
    justify-content: center;
    font-family: "Cinzel", serif;
    font-weight: 700;
    font-size: 64px;
    color: var(--gold);
  }
  .wordmark {
    position: absolute;
    left: 0;
    right: 0;
    top: 268px;
    font-family: "Cinzel", serif;
    font-weight: 700;
    font-size: 84px;
    letter-spacing: 3px;
    color: var(--gold);
    line-height: 1;
  }
  .vintage-row {
    position: absolute;
    left: 0;
    right: 0;
    top: 390px;
    height: 50px;
  }
  .flourish {
    position: absolute;
    top: 4px;
    width: 140px;
    height: 42px;
  }
  .flourish.left { left: 177px; }
  .flourish.right { left: 460px; }
  .vintage {
    position: absolute;
    left: 0;
    right: 0;
    top: 0;
    font-family: "Libre Baskerville", serif;
    font-weight: 400;
    font-size: 38px;
    color: var(--ink);
    line-height: 1.2;
  }
  .region {
    position: absolute;
    left: 0;
    right: 0;
    top: 452px;
    font-family: "Libre Baskerville", serif;
    font-size: 19px;
    letter-spacing: 1.5px;
    color: var(--ink-soft);
  }
  .varietal {
    position: absolute;
    left: 0;
    right: 0;
    top: 482px;
    font-family: "Libre Baskerville", serif;
    font-size: 30px;
    letter-spacing: 1.5px;
    color: var(--ink);
  }
  .origin {
    position: absolute;
    left: 0;
    right: 0;
    top: 540px;
    font-family: "Pinyon Script", cursive;
    font-size: 36px;
    color: var(--ink-soft);
  }
  .landscape {
    position: absolute;
    left: 0;
    bottom: 0;
    width: 770px;
    height: 366px;
    background:
      linear-gradient(180deg,
        rgba(244,248,251,0) 0%,
        var(--mountain) 12%,
        var(--mountain-shade) 45%,
        #8fa07a 58%,
        var(--vine-light) 68%,
        var(--vine-dark) 100%);
  }
</style>
</head>
<body>
  <main class="canvas">
    <section class="label">
      <div class="brand-mark">HC</div>
      <h1 class="wordmark">Harbor Crest</h1>
      <div class="vintage-row">
        <div class="flourish left" role="img" aria-label="Decorative scroll flourish" style="background: radial-gradient(ellipse at center, rgba(154,154,154,0.55) 0%, rgba(154,154,154,0) 70%);"></div>
        <p class="vintage">2015</p>
        <div class="flourish right" role="img" aria-label="Decorative scroll flourish" style="background: radial-gradient(ellipse at center, rgba(154,154,154,0.55) 0%, rgba(154,154,154,0) 70%);"></div>
      </div>
      <p class="region">WAITAKI VALLEY—NORTH OTAGO</p>
      <p class="varietal">PINOT GRIS</p>
      <p class="origin">New Zealand Wine</p>
      <div class="landscape" role="img" aria-label="Photograph of misty mountains above a green vineyard with farm buildings in the Waitaki Valley"></div>
    </section>
  </main>
</body>
</html>
```